Business Card Design

I design and sell kitchens. I would like the card to have a black background either gloss or matt and a stripe through the middle in deep sky blue, the same blue as the team ridgeway pro cycling team. Written in the blue stripe in white i would like Harbourline kitchens in italics. underneath the stripe, again in white i would like 'the complete design and installation service. On the reverse i would like the following in simple black on white
Owen Tramley
07814 296540
email- owentramley@harbourlinekitchens-example.co.uk
Web- WWW.harbourlinekitchens-example.co.uk

I have added a copy of an initial idea for a logo but it can be changed to suit the brief above

Industry/Entity Type

Business

Contact Information for Business Card

Harbourline Kitchens
The complete design and installation service
Owen Tramley
07814 296540-mob
owentramley@harbourlinekitchen-example.co.uk
WWW.harbourlinekitchens-example.co.uk

```html
<!DOCTYPE html>
<html lang="en">
<head>
<meta charset="utf-8">
<title>Harbourline Kitchens – Business Card</title>
<link rel="stylesheet" href="https://fonts.googleapis.com/css2?family=Anton&family=Arimo:wght@400;700&display=swap">
<style>
  :root {
    --backdrop: #e4e0dc;
    --card-black: #231f20;
    --stripe-blue: #35a9df;
    --ink-white: #ffffff;
    --ink-black: #111111;
    --ink-grey: #333333;
  }
  * { box-sizing: border-box; margin: 0; padding: 0; }
  html, body {
    width: 1200px;
    height: 828px;
    overflow: hidden;
    background: var(--backdrop);
  }
  .sheet {
    position: relative;
    width: 1200px;
    height: 828px;
  }
  .card {
    position: absolute;
    top: 239px;
    width: 540px;
    height: 350px;
    border-radius: 24px;
    overflow: hidden;
    box-shadow: 0 6px 18px rgba(0, 0, 0, 0.18);
  }
  .card--front { left: 40px; background: var(--card-black); }
  .card--back { left: 620px; background: var(--ink-white); }

  .stripe {
    position: absolute;
    left: 0;
    right: 0;
    top: 128px;
    height: 100px;
    background: var(--stripe-blue);
  }
  .brand-name {
    position: absolute;
    left: 0;
    right: 0;
    top: 134px;
    text-align: center;
    font-family: "Anton", sans-serif;
    font-weight: 400;
    color: var(--ink-white);
    font-size: 36px;
    line-height: 42px;
    letter-spacing: 1px;
    text-transform: uppercase;
  }
  .tagline {
    position: absolute;
    left: 0;
    right: 0;
    top: 236px;
    text-align: center;
    font-family: "Anton", sans-serif;
    color: var(--ink-white);
    font-size: 13px;
    letter-spacing: 1.6px;
    text-transform: uppercase;
  }

  .holder {
    position: absolute;
    left: 112px;
    top: 82px;
    font-family: "Arimo", sans-serif;
  }
  .holder-name {
    font-weight: 700;
    font-size: 17px;
    color: var(--ink-black);
  }
  .holder-role {
    font-size: 14px;
    color: var(--ink-grey);
    margin-top: 1px;
  }
  .contacts {
    position: absolute;
    left: 100px;
    top: 168px;
    list-style: none;
    font-family: "Arimo", sans-serif;
    font-size: 13px;
    color: var(--ink-grey);
  }
  .contact {
    display: flex;
    align-items: center;
    height: 28px;
  }
  .contact-icon {
    width: 14px;
    height: 14px;
    margin-right: 18px;
    flex: none;
  }
</style>
</head>
<body>
<main class="sheet">
  <section class="card card--front" aria-label="Card front">
    <div class="stripe"></div>
    <h1 class="brand-name">Harbourline<br>Kitchens</h1>
    <p class="tagline">The complete design and installation service</p>
  </section>

  <section class="card card--back" aria-label="Card back">
    <div class="holder">
      <p class="holder-name">Owen Tramley</p>
      <p class="holder-role">Director</p>
    </div>
    <ul class="contacts">
      <li class="contact">
        <svg class="contact-icon" viewBox="0 0 24 24" aria-hidden="true"><path fill="#111" d="M6.6 10.8a15.1 15.1 0 0 0 6.6 6.6l2.2-2.2a1 1 0 0 1 1-.25 11.4 11.4 0 0 0 3.6.57 1 1 0 0 1 1 1V20a1 1 0 0 1-1 1A17 17 0 0 1 3 4a1 1 0 0 1 1-1h3.5a1 1 0 0 1 1 1c0 1.25.2 2.45.57 3.6a1 1 0 0 1-.25 1z"/></svg>
        <span>07814 296540</span>
      </li>
      <li class="contact">
        <svg class="contact-icon" viewBox="0 0 24 24" aria-hidden="true"><rect x="2" y="5" width="20" height="14" rx="1" fill="#111"/><path d="M3 6l9 7 9-7" fill="none" stroke="#fff" stroke-width="1.8"/></svg>
        <span>owentramley@harbourlinekitchens-example.co.uk</span>
      </li>
      <li class="contact">
        <svg class="contact-icon" viewBox="0 0 24 24" aria-hidden="true"><circle cx="12" cy="12" r="10" fill="#111"/><g fill="none" stroke="#fff" stroke-width="1.4"><ellipse cx="12" cy="12" rx="4" ry="10"/><path d="M2 12h20M4 7h16M4 17h16"/></g></svg>
        <span>www.harbourlinekitchens-example.co.uk</span>
      </li>
    </ul>
  </section>
</main>
</body>
</html>
```